ROLL-ON-VERANDA Business Card Design

Please do not submit more than one design per designer. Both the front and the back must be submitted as a single design. Please use all of the attached files to design a two-sided business card. Do not use tiny text that is hard to read. Do not put text or images too close to the edges where it might get cut off during printing. The card should be horizontal. Please do not send me the same design that I attached showing the business information. Be creative.

One file is marked as the primary logo for company. Other files are marked as secondary. All logos should be incorporated into the design with a focus on the primary one being bigger.

```html
<!DOCTYPE html>
<html lang="en">
<head>
<meta charset="utf-8">
<title>ROLL-ON-VERANDA Business Card</title>
<link href="https://fonts.googleapis.com/css2?family=Russo+One&family=Marcellus&display=swap" rel="stylesheet">
<style>
  :root {
    --backdrop: #d9d6d1;
    --card: #ffffff;
    --card-shade: #ececec;
    --ink: #111111;
    --ink-soft: #6a6a6a;
    --rule: #3a3a3a;
    --mark: #2a2a2a;
    --navy: #1d2a6b;
    --red: #c8202f;
    --gold: #c9a233;
    --teal: #3b7fa8;
  }
  * { box-sizing: border-box; margin: 0; padding: 0; }
  html, body { width: 1200px; height: 900px; overflow: hidden; }
  body {
    background: var(--backdrop);
    position: relative;
    font-family: "Marcellus", serif;
    color: var(--ink);
  }
  .card {
    position: absolute;
    left: 300px;
    width: 600px;
    height: 343px;
    background: linear-gradient(135deg, var(--card) 0%, var(--card) 55%, var(--card-shade) 100%);
    border-bottom: 10px solid var(--ink);
    box-shadow: 0 8px 22px rgba(0,0,0,0.25);
    overflow: hidden;
  }
  .card--logo { top: 60px; }
  .card--contact { top: 470px; }

  .brand { position: absolute; display: flex; align-items: center; }
  .brand__mark { background: var(--mark); flex: none; }
  .wordmark {
    font-family: "Russo One", sans-serif;
    color: var(--ink);
    letter-spacing: 1px;
    white-space: nowrap;
  }

  .card--logo .brand { left: 40px; top: 48px; gap: 16px; }
  .card--logo .brand__mark { width: 88px; height: 88px; }
  .card--logo .wordmark { font-size: 34px; }

  .rule { position: absolute; height: 1px; background: var(--rule); }
  .card--logo .rule--top { left: 330px; right: 36px; top: 156px; }
  .card--logo .rule--bottom { left: 36px; width: 300px; top: 246px; }

  .badge { position: absolute; border-radius: 50%; }
  .badge--anchor { left: 500px; top: 172px; width: 58px; height: 58px; background: var(--ink); border: 4px solid var(--gold); }
  .badge--vob { left: 400px; top: 182px; width: 54px; height: 54px; background: var(--navy); border: 4px solid var(--red); }
  .badge--guard { left: 250px; top: 176px; width: 56px; height: 56px; background: var(--navy); border: 3px solid var(--gold); }
  .badge--council { left: 58px; top: 258px; width: 48px; height: 48px; background: #fff; border: 4px solid var(--teal); }
  .badge-caption {
    position: absolute; left: 46px; top: 310px;
    font-family: "Russo One", sans-serif; font-size: 9px; color: var(--teal); letter-spacing: .5px;
  }

  .person { position: absolute; left: 40px; top: 24px; }
  .person__name { font-family: "Russo One", sans-serif; font-size: 22px; letter-spacing: .5px; }
  .person__creds { font-size: 14px; color: var(--ink-soft); line-height: 1.35; margin-top: 4px; }

  .card--contact .brand { left: 0; right: 0; top: 104px; justify-content: center; gap: 14px; }
  .card--contact .brand__mark { width: 64px; height: 64px; }
  .card--contact .wordmark { font-size: 30px; }

  .tagline {
    position: absolute; left: 40px; right: 40px; top: 186px; text-align: center;
    font-family: "Marcellus", serif; font-weight: 400; font-size: 13px; letter-spacing: .6px;
    text-transform: uppercase; line-height: 1.4;
  }
  .card--contact .rule { left: 40px; right: 40px; top: 240px; }
  .contacts {
    position: absolute; left: 40px; right: 40px; top: 256px;
    display: flex; justify-content: space-between; align-items: center;
    font-size: 13px; color: var(--ink-soft); list-style: none;
  }
  .contacts li { display: flex; align-items: center; gap: 6px; }
  .contacts svg { width: 14px; height: 14px; fill: var(--ink); }
</style>
</head>
<body>

<section class="card card--logo" aria-label="Card front">
  <div class="brand">
    <div class="brand__mark" role="img" aria-label="Company logo mark"></div>
    <div class="wordmark">ROLL-ON-VERANDA</div>
  </div>
  <div class="rule rule--top"></div>
  <div class="rule rule--bottom"></div>
  <div class="badge badge--anchor" role="img" aria-label="Training company badge"></div>
  <div class="badge badge--vob" role="img" aria-label="Veteran owned business badge"></div>
  <div class="badge badge--guard" role="img" aria-label="Licensed captain badge"></div>
  <div class="badge badge--council" role="img" aria-label="Boating council badge"></div>
  <div class="badge-caption">INSTRUCTOR</div>
</section>

<section class="card card--contact" aria-label="Card back">
  <div class="person">
    <h1 class="person__name">CAPTAIN DANA R. WHITLOCK</h1>
    <p class="person__creds">CMLA Licensed Master Captain | NBTA Certified Instructor<br>Graduate Degree | Veteran</p>
  </div>
  <div class="brand">
    <div class="brand__mark" role="img" aria-label="Company logo mark"></div>
    <div class="wordmark">ROLL-ON-VERANDA</div>
  </div>
  <p class="tagline">Providing hands-on boat training,<br>captaining services and deliveries in the Seabright County area.</p>
  <div class="rule"></div>
  <ul class="contacts">
    <li><svg viewBox="0 0 16 16"><circle cx="8" cy="8" r="7" fill="none" stroke="#111" stroke-width="1.6"/><path d="M1 8h14M8 1c-3 3-3 11 0 14M8 1c3 3 3 11 0 14" fill="none" stroke="#111" stroke-width="1.2"/></svg>www.Roll-On-Veranda.com</li>
    <li><svg viewBox="0 0 16 16"><rect x="1" y="3" width="14" height="10" rx="1"/><path d="M1 4l7 5 7-5" fill="none" stroke="#fff" stroke-width="1.3"/></svg>service@rollonveranda.com</li>
    <li><svg viewBox="0 0 16 16"><path d="M4 1l3 3-2 2c1 2 3 4 5 5l2-2 3 3-2 3C7 15 1 9 1 3z"/></svg>(555)014-2290</li>
  </ul>
</section>

</body>
</html>
```